Harbor Crew Biz Cards

looking for a new catchy business card where my cell number is very prominent:
My pic and logo are attached. My whole picture isn't necessary if it makes more sense to crop it.

Info needed:

(Big) Marcus Pellton
(Medium) Real Estate Professional
(Medium) Buyer/Seller Specialist
(Big) Call/Text 410-739-2184
(small) Marcuspell@mailbrook.com
(small) www.harborcrewhomes.com

(very small)
The Harbor Crew
at Keystone Real Estate
2847 W Larkmoor Rd, Bel Air, MD 21014
833-555-0192

```html
<!DOCTYPE html>
<html lang="en">
<head>
<meta charset="utf-8">
<title>Harbor Crew Business Cards</title>
<link rel="stylesheet" href="https://fonts.googleapis.com/css2?family=Tinos:wght@400;700&display=swap">
<style>
  :root {
    --navy: #1c2c5b;
    --text-gray: #555a60;
    --rule-gray: #8a8f99;
    --soft-gray: #eceef2;
    --card-white: #ffffff;
    --backdrop: #e7e4df;
    --photo-light: #c9ccd3;
    --photo-dark: #3a4766;
  }
  * { margin: 0; padding: 0; box-sizing: border-box; }
  html, body { width: 900px; height: 1200px; overflow: hidden; }
  body {
    position: relative;
    background: var(--backdrop);
    font-family: "Tinos", "Times New Roman", serif;
    color: var(--text-gray);
  }
  .card {
    position: absolute;
    left: 77px;
    width: 748px;
    height: 438px;
    background: var(--card-white);
    overflow: hidden;
  }
  .card--front { top: 125px; }
  .card--back { top: 657px; }
  .card__band {
    position: absolute;
    left: 0; right: 0; bottom: 0;
    height: 20px;
    background: var(--navy);
  }
  .agent-name {
    position: absolute;
    left: 44px; top: 53px;
    font-size: 31px; font-weight: 700;
    color: var(--navy);
    letter-spacing: 0.5px;
  }
  .agent-role {
    position: absolute;
    left: 44px; top: 87px;
    font-size: 18px; line-height: 24px;
  }
  .agent-phone {
    position: absolute;
    left: 44px; top: 142px;
    font-size: 28px; font-weight: 700;
    color: var(--navy);
    letter-spacing: 0.3px;
  }
  .agent-links {
    position: absolute;
    left: 44px; top: 177px;
    font-size: 17px; line-height: 25px;
  }
  .office {
    position: absolute;
    left: 44px; top: 311px;
    font-size: 13px; line-height: 20px;
    font-style: normal;
  }
  .office__icon { width: 9px; height: 9px; vertical-align: -1px; margin-right: 4px; }
  .agent-photo {
    position: absolute;
    left: 410px; top: 15px;
    width: 294px; height: 423px;
    border-radius: 110px 110px 0 0;
    background: linear-gradient(180deg, var(--photo-light) 0%, var(--photo-dark) 40%, var(--navy) 100%);
  }
  .back-accent {
    position: absolute;
    right: -60px; top: 40px;
    width: 300px; height: 300px;
    border-radius: 50%;
    background: var(--soft-gray);
  }
  .brand {
    position: absolute;
    left: 0; right: 0; top: 88px;
    text-align: center;
  }
  .brand__mark {
    display: block;
    margin: 0 auto 42px;
    width: 140px; height: 140px;
    border-radius: 50%;
    background: var(--navy);
  }
  .brand__name {
    font-size: 42px; font-weight: 400;
    color: var(--navy);
    letter-spacing: 2px;
    text-transform: uppercase;
    line-height: 1;
  }
  .brand__tagline {
    display: inline-flex;
    align-items: center;
    gap: 12px;
    margin-top: 12px;
    font-size: 13px;
    letter-spacing: 2.5px;
    color: var(--navy);
    text-transform: uppercase;
  }
  .brand__tagline::before,
  .brand__tagline::after {
    content: "";
    width: 28px; height: 1px;
    background: var(--navy);
  }
</style>
</head>
<body>
  <section class="card card--front">
    <h1 class="agent-name">MARCUS PELLTON</h1>
    <p class="agent-role">Real Estate Professional<br>Buyer/Seller Specialist</p>
    <p class="agent-phone">CALL/TEXT 410-739-2184</p>
    <p class="agent-links">Marcuspell@mailbrook.com<br>www.harborcrewhomes.com</p>
    <address class="office">
      THE HARBOR CREW<br>
      AT KEYSTONE REAL ESTATE<br>
      2847 W Larkmoor Rd, Bel Air, MD 21014<br>
      <svg class="office__icon" viewBox="0 0 10 10" aria-hidden="true"><path d="M2 0.5 L3.8 2.6 L2.9 3.6 Q4 6 6.4 7.1 L7.4 6.2 L9.5 8 L8.3 9.5 Q3.5 9 0.5 1.7 Z" fill="currentColor"/></svg>833-555-0192
    </address>
    <div class="card__band"></div>
    <div class="agent-photo" role="img" aria-label="Portrait photo of the agent in a navy suit"></div>
  </section>

  <section class="card card--back">
    <div class="back-accent"></div>
    <div class="brand">
      <span class="brand__mark"></span>
      <p class="brand__name">The Harbor Crew</p>
      <p class="brand__tagline">at Keystone Real Estate</p>
    </div>
    <div class="card__band"></div>
  </section>
</body>
</html>
```